Chewing Gum With Active Ingredients Needs Packaging Design

Brivelle Gum Science is a revolutionary new chewing gum that contains active ingredients commonly found in mouthwashes - it's a portable and convenient way to keep a fresh, clean, and healthy mouth. We have a thorough design brief (attached file) for the packaging we need - a simple sleeve for blister packed gum. We want our design to convey that we are a modern, effective, and high-end product.

Target Market(s)

Young professionals, 20-35 years old

Font styles to use
Serif
Sans Serif

Colors
0292cd
ffffff
0555a3

Requirements
Must have
• A sleek, elegant design
• ALL of the elements listed in the creative brief PDF
• Attached logo
Nice to have
• Incorporation of foil into the design
• A unique, unmistakable look
Should not have
• Too medical of a look

```html
<!DOCTYPE html>
<html lang="en">
<head>
<meta charset="utf-8">
<title>Brivelle Gum Science – Sleeve Dieline</title>
<link href="https://fonts.googleapis.com/css2?family=Josefin+Sans:wght@300;400;600&family=Roboto+Condensed:wght@400;700&display=swap" rel="stylesheet">
<style>
  :root{
    --navy-deep:#040b17;
    --navy:#0a2649;
    --blue:#0555a3;
    --cyan:#0292cd;
    --white:#ffffff;
    --soft-white:#dfe6ee;
    --trim:#e07a1f;
    --glue:#dcdcdc;
    --warn:#e0201a;
    --guide:#2aa0e0;
  }
  *{box-sizing:border-box;margin:0;padding:0}
  html,body{width:800px;height:1200px;overflow:hidden;background:var(--white)}
  body{position:relative;font-family:"Josefin Sans",sans-serif;color:var(--white)}

  .sleeve{position:absolute;left:20px;top:70px;width:760px;height:1057px;border:1px solid var(--guide);overflow:hidden}
  .panel{position:absolute;left:0;width:100%}
  .back-panel{top:0;height:451px;
    background:
      linear-gradient(160deg,rgba(5,85,163,.55) 0%,transparent 35%),
      linear-gradient(200deg,transparent 45%,rgba(5,85,163,.45) 70%,transparent 90%),
      linear-gradient(180deg,var(--navy) 0%,var(--navy-deep) 100%);}
  .fold-band{top:451px;height:50px;background:linear-gradient(90deg,#071a33,#0b2f5b 60%,#071a33);border-top:1px dashed rgba(255,255,255,.25);border-bottom:1px dashed rgba(255,255,255,.25)}
  .front-panel{top:501px;height:443px;
    background:
      radial-gradient(ellipse 60% 30% at 70% 30%,rgba(2,146,205,.55),transparent 70%),
      linear-gradient(165deg,var(--navy-deep) 0%,#081d3a 40%,var(--blue) 75%,var(--navy) 100%);}
  .tagline-band{top:944px;height:59px;background:linear-gradient(90deg,#0a2c57,#06203f 70%,#0a2c57);border-top:1px dashed rgba(255,255,255,.2)}
  .glue-area{top:1003px;height:54px;background:var(--glue)}

  .flip{position:absolute;transform:rotate(180deg)}

  .web-address{left:261px;top:42px;width:232px;font-size:15px;letter-spacing:.5px;text-align:left}
  .distributor{left:236px;top:190px;width:196px;font-size:14px;line-height:18px;text-align:left;letter-spacing:.3px}
  .back-claims{left:86px;top:276px;width:346px;font-size:14.5px;line-height:21px;text-align:left;letter-spacing:.3px}

  .icon-row{position:absolute;left:266px;top:133px;display:flex;gap:12px}
  .icon-tile{width:44px;height:44px;border-radius:9px;background:var(--white);display:flex;align-items:center;justify-content:center}
  .disposal-icons{position:absolute;left:96px;top:140px;display:flex;gap:12px}

  .drug-facts{left:447px;top:91px;width:194px;height:330px;background:#000;border:2px solid var(--white);font-family:"Roboto Condensed",sans-serif;font-size:7.5px;line-height:9.5px;padding:4px 5px;color:var(--white)}
  .drug-facts h3{font-size:11px;font-style:italic;font-weight:700;border-bottom:3px solid var(--white);padding-bottom:2px;margin-bottom:2px}
  .drug-facts .row{display:flex;justify-content:space-between;font-style:italic;font-size:9px;line-height:10px}
  .drug-facts .active{background:var(--blue);display:flex;justify-content:space-between;padding:1px 2px;margin:3px 0;border-bottom:2px solid var(--white)}
  .drug-facts h4{font-size:9.5px;font-style:italic;font-weight:700;margin-top:4px;border-top:1px solid var(--white);padding-top:2px}
  .drug-facts ul{list-style:none;columns:2;column-gap:6px}
  .drug-facts li::before{content:"■ ";font-size:6px}
  .drug-facts p{margin-top:2px}

  .plaque-stat{left:213px;top:462px;width:486px;height:30px;display:flex;align-items:center;gap:14px;font-size:16px;letter-spacing:3px}
  .ring{width:28px;height:28px;border:2.5px solid var(--white);border-radius:50%;flex:none}

  .pack-details{position:absolute;right:45px;top:516px;text-align:right;font-size:17px;line-height:22px;font-weight:400;letter-spacing:.3px}
  .brand-ring{position:absolute;left:459px;top:656px;width:66px;height:66px;border:4px solid var(--white);border-radius:50%}
  .brand-name{position:absolute;left:150px;top:748px;width:580px;text-align:center;font-size:72px;font-weight:300;letter-spacing:8px;color:var(--soft-white);line-height:80px}
  .brand-sub{position:absolute;left:168px;top:830px;width:560px;text-align:center;font-size:20px;font-weight:300;letter-spacing:16px;color:var(--soft-white)}
  .benefits{position:absolute;top:878px;font-size:17px;line-height:22px;letter-spacing:.3px}
  .benefits.left{right:264px;text-align:right}
  .benefits.right{left:520px;text-align:left}
  .gum-visual{position:absolute;left:37px;top:819px;width:107px;height:112px;border-radius:14px;background:linear-gradient(145deg,#ffffff,#c9d3dc)}

  .tagline{position:absolute;left:58px;top:958px;display:flex;align-items:center;gap:18px;font-size:17px;letter-spacing:4px}

  .glue-note{position:absolute;left:72px;top:1010px;display:flex;align-items:center;gap:6px;font-size:14px;color:var(--warn)}

  .dieline{position:absolute;left:0;top:0;pointer-events:none}
</style>
</head>
<body>
<main class="sleeve">
  <section class="panel back-panel" aria-label="Back panel"></section>
  <section class="panel fold-band" aria-label="Top fold"></section>
  <section class="panel front-panel" aria-label="Front panel"></section>
  <section class="panel tagline-band" aria-label="Bottom fold"></section>
  <section class="panel glue-area" aria-label="Adhesive area"></section>

  <p class="flip web-address">WWW.BRIVELLEGUM.COM</p>

  <div class="flip drug-facts">
    <h3>Drug Facts</h3>
    <div class="row"><span>Active ingredient<br>(in each caplet)</span><span>Purpose</span></div>
    <div class="active"><span>Acetaminophen 500 mg</span><span>Pain reliever/fever reducer</span></div>
    <h4>Uses</h4>
    <p>■ temporarily relieves minor aches and pains due to:</p>
    <ul>
      <li>the common cold</li><li>headache</li><li>backache</li><li>minor pain of arthritis</li>
      <li>toothache</li><li>muscular aches</li><li>premenstrual cramps</li>
    </ul>
    <p>■ temporarily reduces fever</p>
    <h4>Warnings</h4>
    <p><b>Liver warning:</b> this product contains acetaminophen. Severe liver damage may occur if you take too much.</p>
    <p><b>Allergy alert:</b> may cause severe skin reactions.</p>
    <p><b>Do not use</b> with other drugs containing acetaminophen.</p>
    <p><b>Ask a doctor before use</b> if you have liver disease.</p>
  </div>

  <div class="flip icon-row" aria-label="Usage icons">
    <span class="icon-tile"><svg width="26" height="26"><circle cx="13" cy="13" r="10" fill="#0a2649"/></svg></span>
    <span class="icon-tile"><svg width="26" height="26"><rect x="10" y="3" width="6" height="20" rx="2" fill="#0a2649"/></svg></span>
    <span class="icon-tile"><svg width="26" height="26"><circle cx="13" cy="13" r="10" fill="none" stroke="#0a2649" stroke-width="3"/></svg></span>
  </div>

  <div class="flip disposal-icons" aria-label="Disposal icons">
    <svg width="30" height="36"><rect x="8" y="4" width="14" height="28" rx="3" fill="#ffffff"/></svg>
    <svg width="36" height="36"><circle cx="18" cy="18" r="15" fill="none" stroke="#ffffff" stroke-width="3"/><circle cx="18" cy="18" r="7" fill="#ffffff"/></svg>
  </div>

  <p class="flip distributor">DIST BY NORLAND INDUSTRIES:<br>AURORA, CO QUESTIONS?<br>XXX-XXX-XXXX</p>

  <p class="flip back-claims">WITH FDA-APPROVED ACTIVE INGREDIENTS,<br>DENTIST-RECOMMENDED BRIVELLE GUM<br>WHITENS TEETH, FRESHENS BREATH,<br>AND HELPS REDUCE PLAQUE<br>AND PREVENT GINGIVITIS</p>

  <div class="flip plaque-stat"><span class="ring"></span><span>2 IN 3 ADULTS HAVE VISIBLE PLAQUE</span></div>

  <p class="pack-details">8 PIECES SUGAR FREE GUM<br>ASPARTAME FREE WITH XYLITOL<br>PEPPERMINT</p>

  <span class="brand-ring"></span>
  <h1 class="brand-name">BRIVELLE</h1>
  <p class="brand-sub">GUM SCIENCE</p>

  <p class="benefits left">WHITENS TEETH<br>HELPS REDUCE PLAQUE</p>
  <p class="benefits right">FRESHENS BREATH<br>HELPS PROTECT GUMS</p>

  <div class="gum-visual" role="img" aria-label="Two white gum pellets"></div>

  <div class="tagline"><span class="ring"></span><span>CONFIDENCE GUARANTEED</span></div>

  <p class="glue-note">
    <svg width="12" height="40" viewBox="0 0 12 40"><path d="M6 2V38M2 7L6 2L10 7M2 33L6 38L10 33" stroke="#222" stroke-width="1.4" fill="none"/></svg>
    NO TEXT OR ART HERE IN GRAY AREA - packaging adhesive will be applied here!
  </p>

  <svg class="dieline" width="760" height="1057" viewBox="0 0 760 1057" aria-hidden="true">
    <path d="M15 15H745V155A75 75 0 0 0 745 305V1040H15V305A75 75 0 0 0 15 155Z" fill="none" stroke="var(--trim)" stroke-width="1.5" stroke-dasharray="5 4"/>
  </svg>
</main>
</body>
</html>
```